Offer banner redesign / Simplifying existing banner

We have a banner there customer can click on to get an offer. We want to simplify this banner and to get it to at minimum. We are not clear about how it shoulderstand look like, but the actual banner you can see here (It's at the top of the page): https://ofenrohr-lagerhaus.de/kaminsysteme/ We want to get rid of the icons and to reduce the size of the baner. The baner shoulderstand contain the Following text: Affordable chimney using installation service button text: Request free quote

Target Market(s)

Customers from age of 40yrs.

Requirements
Must have
• Clear and good visible button
Nice to have
• It Should be simple and striking.

```html
<!DOCTYPE html>
<html lang="de">
<head>
<meta charset="utf-8">
<title>Angebots-Banner – Entwürfe</title>
<link rel="stylesheet" href="https://fonts.googleapis.com/css2?family=Arimo:wght@400;700&family=Roboto+Condensed:wght@700&display=swap">
<style>
  :root {
    --page-bg: #d9dbda;
    --banner-bg: #ffffff;
    --stripe: #fbb03b;
    --accent: #f07d10;
    --text-dark: #111111;
    --pill-top: #fdbb4a;
    --pill-bottom: #f39a1c;
    --pill-edge: #b86c10;
    --ring-light: #ffffff;
    --ring-dark: #c9c9c9;
    --knob-light: #f58a2a;
    --knob-dark: #a93f02;
  }
  * { box-sizing: border-box; margin: 0; padding: 0; }
  html, body { width: 1200px; height: 587px; overflow: hidden; }
  body {
    background: var(--page-bg);
    font-family: "Arimo", Arial, sans-serif;
    position: relative;
  }
  .banner {
    position: absolute;
    left: 99px;
    width: 1017px;
    background: var(--banner-bg);
  }
  .banner--flat { top: 122px; height: 133px; }
  .banner--shadow { top: 320px; height: 137px; }

  .stripe-top, .stripe-bottom { position: absolute; left: 0; right: 0; }
  .stripe-top {
    top: 0; height: 14.5px;
    background: repeating-linear-gradient(90deg, var(--stripe) 0 14.5px, transparent 14.5px 21.8px);
  }
  .stripe-bottom {
    bottom: 0; height: 6px;
    background: repeating-linear-gradient(90deg, var(--stripe) 0 20px, transparent 20px 27.4px);
  }
  .banner--shadow .stripe-top,
  .banner--shadow .stripe-bottom {
    filter: drop-shadow(0 3px 1.5px rgba(0,0,0,.55));
  }
  .banner--shadow .stripe-top { width: 1017px; }

  .headline {
    position: absolute;
    color: var(--text-dark);
    font-weight: 700;
    font-size: 17.5px;
    line-height: 19px;
  }
  .banner--flat .headline { left: 62px; top: 37px; }
  .banner--shadow .headline { left: 50px; top: 40px; }
  .headline__accent {
    display: block;
    color: var(--accent);
    font-size: 31px;
    line-height: 36px;
    letter-spacing: -0.3px;
  }

  .offer-button {
    position: absolute;
    width: 371px;
    height: 39px;
    border-radius: 20px;
    background: linear-gradient(var(--pill-top), var(--pill-bottom));
    box-shadow: 0 2px 0 var(--pill-edge), 0 3px 4px rgba(0,0,0,.35);
    color: var(--text-dark);
    font-weight: 700;
    font-size: 17.5px;
    text-decoration: none;
  }
  .banner--flat .offer-button { left: 465px; top: 47.5px; }
  .banner--shadow .offer-button { left: 465px; top: 51px; }
  .offer-button__left, .offer-button__right {
    position: absolute; top: 10px;
  }
  .offer-button__left { left: 19px; }
  .offer-button__right { left: 254px; }
  .offer-button__knob {
    position: absolute;
    left: 132px; top: -37.5px;
    width: 114px; height: 114px;
  }
  .knob-label {
    font-family: "Roboto Condensed", "Arial Narrow", sans-serif;
    font-weight: 700;
    font-size: 19px;
    fill: #ffffff;
  }
  .variant-number {
    position: absolute;
    left: 590px;
    width: 20px;
    text-align: center;
    font-size: 19px;
    color: var(--text-dark);
  }
  .variant-number--one { top: 273px; }
  .variant-number--two { top: 481px; }
</style>
</head>
<body>
  <svg width="0" height="0" style="position:absolute" aria-hidden="true">
    <defs>
      <linearGradient id="ring-grad" x1="0" y1="0" x2="0" y2="1">
        <stop offset="0" stop-color="var(--ring-light)"/>
        <stop offset="1" stop-color="var(--ring-dark)"/>
      </linearGradient>
      <radialGradient id="knob-grad" cx="0.45" cy="0.3" r="0.75">
        <stop offset="0" stop-color="var(--knob-light)"/>
        <stop offset="0.55" stop-color="#d45d0c"/>
        <stop offset="1" stop-color="var(--knob-dark)"/>
      </radialGradient>
      <linearGradient id="gloss-grad" x1="0" y1="0" x2="0" y2="1">
        <stop offset="0" stop-color="#ffffff" stop-opacity=".45"/>
        <stop offset="1" stop-color="#ffffff" stop-opacity="0"/>
      </linearGradient>
      <symbol id="offer-knob" viewBox="0 0 114 114">
        <circle cx="57" cy="58" r="56" fill="rgba(0,0,0,.25)"/>
        <circle cx="57" cy="57" r="56" fill="url(#ring-grad)"/>
        <circle cx="57" cy="57" r="47" fill="#bdbdbd"/>
        <circle cx="57" cy="57" r="45" fill="url(#knob-grad)"/>
        <ellipse cx="57" cy="32" rx="30" ry="17" fill="url(#gloss-grad)"/>
        <text class="knob-label" x="57" y="64" text-anchor="middle" transform="rotate(-17 57 57)">ANGEBOT</text>
      </symbol>
    </defs>
  </svg>

  <section class="banner banner--flat">
    <div class="stripe-top"></div>
    <p class="headline">Preiswerter Schornstein<br>wahlweise mit<span class="headline__accent">Montageservice</span></p>
    <a class="offer-button" href="#angebot">
      <span class="offer-button__left">kostenloses</span>
      <svg class="offer-button__knob"><use href="#offer-knob"/></svg>
      <span class="offer-button__right">anfordern</span>
    </a>
    <div class="stripe-bottom"></div>
  </section>
  <div class="variant-number variant-number--one">1</div>

  <section class="banner banner--shadow">
    <div class="stripe-top"></div>
    <p class="headline">Preiswerter Schornstein<br>wahlweise mit<span class="headline__accent">Montageservice</span></p>
    <a class="offer-button" href="#angebot">
      <span class="offer-button__left">kostenloses</span>
      <svg class="offer-button__knob"><use href="#offer-knob"/></svg>
      <span class="offer-button__right">anfordern</span>
    </a>
    <div class="stripe-bottom"></div>
  </section>
  <div class="variant-number variant-number--two">2</div>
</body>
</html>
```